Advertising poster for podcast event

"The Lantern Table" is one of the most popular podcasts in Switzerland (https://listen.harbofeed.example/show/4kqpVXRT219LmNaw8BYdE5). It is hosted by the two radio DJs Lukas Brenner and Rafael Tanner. For a series of live shows where the podcast is recorded with an audience, we need a design of a poster. This should have the format A3 high. In addition, the image must be used that was uploaded here, because this is the cover photo with which you can always recognize the podcast. But what is designed around it is up to you. In addition, it must contain the following text:

- Title of the event:
The lantern table - Live
- Show dates:
Saturday, November 11, 2023 - Solothurn
Wednesday, December 27, 2023 - Berne
Thursday, December 28, 2023 - Berne
- A line with additional information about the presale:
The Dome, information and tickets: www.kuppelfest.example

Target Market(s)

Switzerland

Industry/Entity Type

Entertainment

Requirements
Must have
• The attached image and text according to the briefing.

```html
<!DOCTYPE html>
<html lang="en">
<head>
<meta charset="utf-8">
<title>The Lantern Table – Live</title>
<link rel="stylesheet" href="https://fonts.googleapis.com/css2?family=Archivo+Black&family=Bebas+Neue&family=Montserrat:ital,wght@1,900&display=swap">
<style>
  :root {
    --mat: #000000;
    --blue-top: #0a56ad;
    --blue-mid: #3b52a8;
    --blue-low: #1f63b4;
    --blue-bottom: #0a8bd6;
    --sky: #5ac8ec;
    --white: #ffffff;
    --red: #d8141c;
    --red-dark: #a90d14;
    --hero-light: #c9c6dc;
  }
  * { margin: 0; padding: 0; box-sizing: border-box; }
  html, body { width: 904px; height: 1200px; overflow: hidden; background: var(--mat); }
  .canvas { position: relative; width: 904px; height: 1200px; background: var(--mat); }
  .poster {
    position: absolute; left: 92px; top: 89px; width: 720px; height: 1021px; overflow: hidden;
    background: linear-gradient(180deg, var(--blue-top) 0%, #1c4fa8 40%, var(--blue-mid) 60%, var(--blue-low) 78%, var(--blue-bottom) 100%);
  }
  .hosts {
    position: absolute; top: 42px; left: 0; width: 100%;
    font-family: "Bebas Neue", sans-serif; font-weight: 400; color: var(--white); text-align: center;
    font-size: 66px; line-height: 58px; letter-spacing: 0.5px;
  }
  .headphones {
    position: absolute; top: 42px; width: 96px; height: 490px;
    background: linear-gradient(180deg, rgba(180, 190, 235, 0.35), rgba(180, 190, 235, 0));
    border-radius: 40px 40px 0 0;
  }
  .headphones--left { left: 18px; }
  .headphones--right { right: 18px; }
  .hero-art {
    position: absolute; left: 76px; top: 179px; width: 588px; height: 420px;
    border-radius: 200px 200px 0 0;
    background: linear-gradient(180deg, var(--hero-light) 0%, #9f9abc 55%, rgba(91, 86, 114, 0) 100%);
    opacity: 0.85;
  }
  .headline { position: absolute; left: 0; top: 520px; width: 720px; height: 270px; }
  .headline text { font-family: "Archivo Black", sans-serif; font-size: 120px; }
  .headline .line-one { fill: var(--white); }
  .headline .line-two { fill: var(--sky); }
  .live-badge {
    position: absolute; left: 419px; top: 748px; width: 110px; height: 39px; border-radius: 20px;
    background: linear-gradient(180deg, var(--red), var(--red-dark));
    font-family: "Montserrat", sans-serif; font-style: italic; font-weight: 900;
    color: var(--white); font-size: 26px; line-height: 39px; text-align: center; letter-spacing: 2px;
  }
  .show-dates { position: absolute; left: 84px; top: 806px; width: 560px; height: 104px; }
  .show {
    position: absolute; top: 0; width: 160px; height: 104px; text-align: center;
    font-family: "Bebas Neue", sans-serif; font-size: 23px; line-height: 28px; color: var(--white);
    padding-top: 12px; white-space: nowrap;
  }
  .show::before {
    content: ""; position: absolute; left: 0; top: 0; width: 100%; height: 100%;
    border-left: 1.5px solid var(--white); border-top: 1.5px solid var(--white);
    border-top-left-radius: 14px;
    -webkit-mask: linear-gradient(135deg, #000 45%, transparent 100%);
            mask: linear-gradient(135deg, #000 45%, transparent 100%);
  }
  .show:nth-child(1) { left: 0; }
  .show:nth-child(2) { left: 194px; }
  .show:nth-child(3) { left: 388px; }
  .show__date { color: var(--sky); }
  .presale {
    position: absolute; left: 50%; top: 958px; transform: translateX(-50%); height: 35px;
    border: 1.5px solid var(--white); border-radius: 18px;
    font-family: "Bebas Neue", sans-serif; font-size: 18px; line-height: 32px; color: var(--white);
    display: flex; align-items: center; white-space: nowrap;
  }
  .presale__label { padding: 0 8px 0 12px; }
  .presale__url {
    background: var(--sky); height: 32px; border-radius: 16px; padding: 0 12px;
    border-left: 1.5px solid var(--white);
  }
</style>
</head>
<body>
<div class="canvas">
  <div class="poster">
    <div class="headphones headphones--left" role="img" aria-label="Faint headphones decoration with a trailing cable"></div>
    <div class="headphones headphones--right" role="img" aria-label="Faint headphones decoration with a trailing cable"></div>

    <h1 class="hosts">DJ Lukas Brenner<br>&amp; DJ Rafael Tanner</h1>

    <div class="hero-art" role="img" aria-label="Podcast cover illustration of the two hosts, grinning, one giving a thumbs up"></div>

    <svg class="headline" viewBox="0 0 720 270" aria-label="The Lantern Table">
      <defs>
        <filter id="title-shadow" x="-5%" y="-5%" width="115%" height="120%">
          <feDropShadow dx="5" dy="5" stdDeviation="3" flood-color="#0a103c" flood-opacity="0.75"/>
        </filter>
      </defs>
      <text class="line-one" x="111" y="106" textLength="516" lengthAdjust="spacingAndGlyphs" filter="url(#title-shadow)">THE LANTERN</text>
      <text class="line-two" x="208" y="213" textLength="326" lengthAdjust="spacingAndGlyphs" filter="url(#title-shadow)">TABLE</text>
    </svg>

    <div class="live-badge">LIVE</div>

    <div class="show-dates">
      <div class="show"><div>Saturday</div><div class="show__date">November 11, 2023</div><div>Solothurn</div></div>
      <div class="show"><div>Wednesday</div><div class="show__date">December 27, 2023</div><div>Berne</div></div>
      <div class="show"><div>Thursday</div><div class="show__date">December 28, 2023</div><div>Berne</div></div>
    </div>

    <div class="presale">
      <span class="presale__label">The Dome, information and tickets:</span>
      <span class="presale__url">www.kuppelfest.example</span>
    </div>
  </div>
</div>
</body>
</html>
```